Post card

I want an educational customer postcard with our logo, email, and contact number. We are a residential foundation inspection & repair company here in Los Angeles. We provide foundation repair, earthquake retrofitting, and reinforcement.
Our number is 323-555-0148.
Email info@bramblecrestworks.com
Our license number is #2839165

OUR GOAL
Our primary objective is to empower clients with comprehensive knowledge about foundation issues and earthquake retrofitting. By educating them on the potential risks associated with foundation problems and the importance of earthquake retrofitting, we aim to equip homeowners with the necessary information to make informed decisions about safeguarding their properties. Highlighting the benefits of having their houses properly bolted not only enhances structural integrity but also provides peace of mind during seismic events, ensuring the safety and security of their homes and loved ones.

```html
<!DOCTYPE html>
<html lang="en">
<head>
<meta charset="utf-8">
<title>Bramblecrest Works – Residential Foundation Inspection &amp; Repair</title>
<link href="https://fonts.googleapis.com/css2?family=Bebas+Neue&family=Montserrat:wght@500;700;800&display=swap" rel="stylesheet">
<style>
  :root {
    --brand-blue: #2f5fb8;
    --brand-red: #c4323c;
    --white: #ffffff;
  }
  * { margin: 0; padding: 0; box-sizing: border-box; }
  html, body { width: 1200px; height: 816px; overflow: hidden; background: var(--white); }
  .postcard {
    position: relative;
    width: 1200px;
    height: 816px;
    overflow: hidden;
    background: var(--white);
    font-family: "Montserrat", sans-serif;
    color: var(--white);
  }
  .backdrop { position: absolute; inset: 0; }

  .brand {
    position: absolute;
    left: 76px;
    top: 50px;
    width: 290px;
    display: flex;
    align-items: center;
    gap: 14px;
  }
  .brand-mark { width: 54px; height: 54px; background: var(--brand-blue); flex-shrink: 0; }
  .brand-name {
    font-family: "Montserrat", sans-serif;
    font-weight: 800;
    font-size: 25px;
    line-height: 1.05;
    color: var(--brand-blue);
    white-space: nowrap;
  }

  .photo-tile {
    position: absolute;
    border: 6px solid var(--white);
    transform: rotate(45deg);
    box-shadow: 0 0 6px rgba(0,0,0,0.35);
  }
  .tile-crack { left: 445px; top: 4px; width: 210px; height: 210px; background: linear-gradient(135deg, #8d8a86, #5e5b57); }
  .tile-bracket { left: 715px; top: 1px; width: 190px; height: 190px; background: linear-gradient(135deg, #ecebe6, #9da3b0); }
  .tile-plywood { left: 590px; top: 147px; width: 190px; height: 190px; background: linear-gradient(135deg, #deae72, #a9774a); }

  .headline {
    position: absolute;
    left: 56px;
    top: 240px;
    width: 334px;
    text-align: center;
    font-family: "Bebas Neue", sans-serif;
    font-weight: 400;
    font-size: 82px;
    line-height: 78px;
    letter-spacing: 0.5px;
    color: var(--white);
  }

  .book-now {
    position: absolute;
    left: 90px;
    top: 578px;
    width: 211px;
    height: 50px;
    border-radius: 25px;
    background: var(--brand-red);
    color: var(--white);
    font-weight: 500;
    font-size: 22px;
    display: flex;
    align-items: center;
    justify-content: center;
  }

  .contact { position: absolute; left: 88px; top: 670px; }
  .contact-row { display: flex; align-items: center; gap: 22px; }
  .contact-icon {
    width: 34px; height: 34px; border-radius: 50%;
    background: var(--white);
    display: flex; align-items: center; justify-content: center;
    flex-shrink: 0;
  }
  .contact-phone { font-weight: 700; font-size: 34px; letter-spacing: 2px; }
  .contact-email { font-weight: 500; font-size: 20px; margin-top: 8px; }
  .license { font-weight: 500; font-size: 18px; margin-top: 14px; margin-left: 7px; }

  .services {
    position: absolute;
    left: 579px;
    top: 670px;
    list-style: none;
    font-family: "Bebas Neue", sans-serif;
    font-size: 40px;
    line-height: 45px;
  }
  .services li { display: flex; align-items: center; gap: 10px; }
  .services li::before {
    content: "";
    width: 10px; height: 10px;
    background: var(--white);
    flex-shrink: 0;
    margin-top: -6px;
  }
</style>
</head>
<body>
<main class="postcard">
  <svg class="backdrop" width="1200" height="816" viewBox="0 0 1200 816">
    <defs>
      <radialGradient id="worker-photo" cx="0.78" cy="0.45" r="0.7">
        <stop offset="0" stop-color="#8a8a8a"/>
        <stop offset="0.3" stop-color="#555555"/>
        <stop offset="0.7" stop-color="#2b2b2b"/>
        <stop offset="1" stop-color="#141414"/>
      </radialGradient>
      <linearGradient id="panel-blend" x1="0" y1="0" x2="1" y2="0.4">
        <stop offset="0" stop-color="#3a66b8"/>
        <stop offset="0.35" stop-color="#c4434f"/>
        <stop offset="0.75" stop-color="#7e5c8f"/>
        <stop offset="1" stop-color="#4a63ae"/>
      </linearGradient>
      <linearGradient id="band-left" x1="0" y1="0" x2="1" y2="0">
        <stop offset="0" stop-color="#c2404c"/>
        <stop offset="1" stop-color="#4b62ad"/>
      </linearGradient>
      <linearGradient id="band-right" x1="0" y1="0" x2="1" y2="0">
        <stop offset="0" stop-color="#c8414a"/>
        <stop offset="0.55" stop-color="#8a5a86"/>
        <stop offset="1" stop-color="#4d63ae"/>
      </linearGradient>
    </defs>

    <polygon class="worker-photo" points="520,0 1200,0 1200,653 384,653 384,163 416,163" fill="url(#worker-photo)" role="img" aria-label="Black and white photo of a worker in a hard hat bolting a sill plate to a foundation in a crawl space"/>

    <polygon class="chevron-red" points="0,163 384,163 653,575 560,653 0,653" fill="var(--brand-red)"/>
    <polygon class="chevron-panel" points="0,163 334,163 598,575 520,653 0,653" fill="url(#panel-blend)"/>

    <polygon class="band-left" points="0,653 557,653 450,816 0,816" fill="url(#band-left)"/>
    <polygon class="band-right" points="570,653 1200,653 1200,816 463,816" fill="url(#band-right)"/>
  </svg>

  <div class="photo-tile tile-crack" role="img" aria-label="Photo of a crack running through a concrete slab"></div>
  <div class="photo-tile tile-bracket" role="img" aria-label="Photo of a steel foundation bracket bolted in place"></div>
  <div class="photo-tile tile-plywood" role="img" aria-label="Photo of a plywood shear wall with vent holes in a crawl space"></div>

  <header class="brand">
    <span class="brand-mark"></span>
    <span class="brand-name">BRAMBLECREST<br>WORKS</span>
  </header>

  <h1 class="headline">Residential<br>Foundation<br>Inspection<br>&amp; Repair</h1>

  <a class="book-now">BOOK NOW</a>

  <section class="contact">
    <div class="contact-row">
      <span class="contact-icon">
        <svg width="20" height="20" viewBox="0 0 24 24"><path d="M6.6 10.8a15.1 15.1 0 0 0 6.6 6.6l2.2-2.2a1 1 0 0 1 1-.25 11.4 11.4 0 0 0 3.6.57 1 1 0 0 1 1 1V20a1 1 0 0 1-1 1A17 17 0 0 1 3 4a1 1 0 0 1 1-1h3.5a1 1 0 0 1 1 1c0 1.25.2 2.45.57 3.57a1 1 0 0 1-.25 1z" fill="var(--brand-red)"/></svg>
      </span>
      <span class="contact-phone">323-555-0148</span>
    </div>
    <div class="contact-row contact-email">
      <span class="contact-icon">
        <svg width="20" height="16" viewBox="0 0 24 18"><rect x="1" y="1" width="22" height="16" rx="1.5" fill="none" stroke="var(--brand-red)" stroke-width="2"/><path d="M1.5 2 12 10.5 22.5 2M1.5 16.5l8-7M22.5 16.5l-8-7" fill="none" stroke="var(--brand-red)" stroke-width="1.8"/></svg>
      </span>
      <span>info@bramblecrestworks.com</span>
    </div>
    <p class="license">License Number is #2839165</p>
  </section>

  <ul class="services">
    <li>Foundation Repair</li>
    <li>Earthquake Retrofitting &amp; Reinforcement</li>
    <li>House Bolting</li>
  </ul>
</main>
</body>
</html>
```